A Book Cover For a Book Called "Tamsire"

Attached are two files for the ISBN bar graph for the print version of the cover! Same image, just two different formats.
Updates

Project Deadline Extended Reason: We'd like to see a few more designs, and work with a few of the designs already submitted. Added Tuesday, October 24, 2017

Target Market(s)

young adult female, parents

Colors

Designer to choose colors to be used in the design.

```html
<!DOCTYPE html>
<html lang="en">
<head>
<meta charset="utf-8">
<title>Tamsire – A Memoir – Book Cover Wrap</title>
<link rel="stylesheet" href="https://fonts.googleapis.com/css2?family=Poiret+One&family=Questrial&family=Arimo&display=swap">
<style>
  :root {
    --page: #ffffff;
    --ink: #000000;
    --gold: #e3d2b3;
    --body-text: #e8d6b2;
    --author-box: #867866;
    --author-box-text: #17120d;
    --glow: #cdbfa8;
  }
  html, body {
    margin: 0;
    padding: 0;
    width: 1200px;
    height: 1200px;
    overflow: hidden;
    background: var(--page);
  }
  .canvas {
    position: relative;
    width: 1200px;
    height: 1200px;
  }
  .wrap-art {
    position: absolute;
    inset: 0;
  }
  .title { font-family: "Poiret One", sans-serif; fill: var(--gold); }
  .subtitle, .byline { font-family: "Questrial", sans-serif; fill: var(--gold); }
  .photo-label { font-family: "Questrial", sans-serif; fill: var(--author-box-text); }
  .blurb {
    position: absolute;
    left: 81px;
    top: 488px;
    width: 446px;
    font-family: "Arimo", sans-serif;
    font-size: 19px;
    line-height: 29.6px;
    color: var(--body-text);
  }
  .blurb p { margin: 0 0 13px 0; }
</style>
</head>
<body>
<div class="canvas">
  <svg class="wrap-art" width="1200" height="1200" viewBox="0 0 1200 1200" xmlns="http://www.w3.org/2000/svg">
    <defs>
      <radialGradient id="front-glow" cx="0.5" cy="0.5" r="0.5">
        <stop offset="0" stop-color="var(--glow)" stop-opacity="0.75"/>
        <stop offset="0.55" stop-color="#6e6252" stop-opacity="0.35"/>
        <stop offset="1" stop-color="#000" stop-opacity="0"/>
      </radialGradient>
      <radialGradient id="back-glow" cx="0.5" cy="0.5" r="0.5">
        <stop offset="0" stop-color="var(--glow)" stop-opacity="0.28"/>
        <stop offset="1" stop-color="#000" stop-opacity="0"/>
      </radialGradient>
      <linearGradient id="reflect-fade" x1="0" y1="0" x2="0" y2="1">
        <stop offset="0" stop-color="var(--gold)" stop-opacity="0.95"/>
        <stop offset="1" stop-color="var(--gold)" stop-opacity="0.7"/>
      </linearGradient>
    </defs>

    <!-- Wrap background band -->
    <rect class="wrap-band" x="0" y="164" width="1200" height="872" fill="var(--ink)"/>

    <!-- Back cover faint image -->
    <ellipse class="back-photo" role="img" aria-label="Faint photo of a ballet dancer's feet en pointe" cx="320" cy="640" rx="150" ry="380" fill="url(#back-glow)"/>

    <!-- Front cover image -->
    <ellipse class="front-photo" role="img" aria-label="Photo of a ballet dancer's feet en pointe on a dark stage" cx="930" cy="660" rx="150" ry="400" fill="url(#front-glow)"/>

    <!-- Back cover -->
    <g class="back-cover">
      <text class="title" x="36" y="304" font-size="91" textLength="220" lengthAdjust="spacingAndGlyphs">TAMSIRE</text>
      <g transform="translate(0,544) scale(1,-0.75)">
        <text class="title" x="36" y="304" font-size="91" textLength="196" lengthAdjust="spacingAndGlyphs" fill="url(#reflect-fade)">TAMSIRE</text>
      </g>
      <rect class="author-photo" x="350" y="242" width="152" height="158" fill="var(--author-box)"/>
      <text class="photo-label" x="426" y="324" font-size="24" text-anchor="middle">PHOTO</text>
      <text class="subtitle" x="36" y="424" font-size="44" textLength="207" lengthAdjust="spacingAndGlyphs">A MEMOIR</text>
      <text class="byline" x="42" y="458" font-size="21" textLength="480" lengthAdjust="spacingAndGlyphs"><tspan font-size="16">BY </tspan>WILLA HART <tspan font-size="16">WITH </tspan>NORA VALE</text>
    </g>

    <!-- Spine -->
    <g class="spine" transform="translate(600,256) rotate(90)">
      <text class="title" x="0" y="0" font-size="51" textLength="120" lengthAdjust="spacingAndGlyphs">TAMSIRE</text>
      <g transform="translate(0,4) scale(1,-0.89)">
        <text class="title" x="0" y="0" font-size="51" textLength="110" lengthAdjust="spacingAndGlyphs">TAMSIRE</text>
      </g>
    </g>
    <g transform="translate(598,552) rotate(90)">
      <text class="subtitle" x="0" y="0" font-size="44" textLength="180" lengthAdjust="spacingAndGlyphs">A MEMOIR</text>
    </g>
    <g transform="translate(578,460) rotate(90)">
      <text class="byline" x="0" y="0" font-size="22" textLength="472" lengthAdjust="spacingAndGlyphs"><tspan font-size="17">BY </tspan>WILLA HART <tspan font-size="17">WITH </tspan>NORA VALE</text>
    </g>

    <!-- Front cover -->
    <g class="front-cover">
      <text class="title" x="696" y="352" font-size="160" textLength="450" lengthAdjust="spacingAndGlyphs">TAMSIRE</text>
      <g transform="translate(0,680.6) scale(1,-0.82)">
        <text class="title" x="696" y="352" font-size="160" textLength="400" lengthAdjust="spacingAndGlyphs" fill="url(#reflect-fade)">TAMSIRE</text>
      </g>
      <text class="subtitle" x="764" y="932" font-size="58" textLength="328" lengthAdjust="spacingAndGlyphs">A MEMOIR</text>
      <text class="byline" x="674" y="979" font-size="25" textLength="476" lengthAdjust="spacingAndGlyphs"><tspan font-size="19">BY </tspan>WILLA HART <tspan font-size="19">WITH </tspan>NORA VALE</text>
    </g>
  </svg>

  <div class="blurb">
    <p>Lorem ipsum dolor sit amet, consetetur sadipscin elitr, sed diam nonumy eirmod tempor invidunt ut labore et dolore magna aliquyam erat, sed diamo voluptua. At vero eos et accusam et justo duo sit dolores et ea rebum. Stet clita kasd gubergren, et sea takimata sanctus est Lorem ipsum dolor situt amet et ea rebum.</p>
    <p>Lorem ipsum dolor sit amet, consetetur sadipscin elitr, sed diam nonumy eirmod tempor invidunt ut labore et dolore magna aliquyam erat, sed diamo voluptua. At vero eos et accusam et justo duo sit dolores et ea rebum. Stet clita kasd gubergren, et sea takimata sanctus est Lorem ipsum dolor situt amet sed diam.</p>
  </div>
</div>
</body>
</html>
```